Parity Skills Forum needs a brochure to attract participants to its trainings

We need a flyer for our EU-funded project called " Parity Skills Forum" and it aims at increasing and developing skills of researchers and university staff members who are implementing measures towards gender equality in their institutions through our offered training programs. The final design should communicate gender equality for Research and Innovation centres and universities. This flyer will be distributed during conferences and events to our audience (mainly gender experts, researchers, administrative staff of universities, etc.) in order to provide the basic information about the project and options to get involved in the different trainings. We are attaching files to provide you with the concrete information on our requirements:- PS Forum flyer content.ppt: includes the content we would like to include in the flyer. There is also the URL to the project website and the different social media channels. - Project logo.zip: the project logo and guidelines as we would like to use colors that belong to the project logo color range. - Partners' logos.zip: Logos that will be included- EU flag: You can download different resolution files of the flag here: https://unionsymbols.example/about/flag_en -Regarding the images or graphics that you may include in the brochure we wouldn’t like to propose any because we do not want to limitate your imagination.

As it was not mentioned and we received a lot of questions about it, we prefer the flyer to be double-sided and in A5

Font styles to use
Serif
Sans Serif

Colors

Designer to choose colors to be used in the design.

Requirements
Nice to have
• At least 4 pages
Should not have
• We would not like to see as dominant colours the classic blue and pink.

```html
<!DOCTYPE html>
<html lang="en">
<head>
<meta charset="utf-8">
<title>PS Forum – A5 bi-fold flyer</title>
<link href="https://fonts.googleapis.com/css2?family=Montserrat:wght@400;500;600;700;800&display=swap" rel="stylesheet">
<style>
:root{
  --bg:#1f3b3d;
  --teal:#22b2c3;
  --teal-dark:#1a98a8;
  --magenta:#c4286b;
  --ink:#3b3f44;
  --grey:#7a7f85;
  --badge:#e4e7ea;
  --paper:#ffffff;
}
*{box-sizing:border-box;margin:0;padding:0}
html,body{width:1200px;height:522px;overflow:hidden}
body{background:var(--bg);font-family:"Montserrat",sans-serif;color:var(--ink);position:relative}
.spread{position:absolute;top:84px;width:500px;height:354px;display:flex}
.spread--outside{left:88px}
.spread--inside{left:612px}
.page{position:relative;width:250px;height:354px;background:var(--paper);overflow:hidden}
.brand{position:absolute;display:flex;align-items:center;gap:8px}
.brand__mark{background:var(--teal);display:block}
.brand__name{font-weight:600;color:var(--ink);letter-spacing:.5px}

/* back cover */
.back .brand{left:26px;top:26px}
.back .brand__mark{width:36px;height:36px}
.back .brand__name{font-size:21px}
.partners__title{position:absolute;top:92px;left:20px;right:20px;display:flex;align-items:center;gap:6px;color:var(--magenta);font-weight:700;font-size:11px;letter-spacing:.5px}
.partners__title::before,.partners__title::after{content:"";flex:1;height:1px;background:var(--magenta)}
.partners__grid{position:absolute;top:116px;left:22px;right:22px;display:grid;grid-template-columns:repeat(4,1fr);gap:10px 12px}
.partners__badge{height:22px;border-radius:4px;background:var(--badge)}
.back__rule{position:absolute;top:213px;left:0;right:0;height:3px;background:var(--magenta)}
.back__contact{position:absolute;top:216px;bottom:0;left:0;right:0;background:var(--teal);padding:18px 16px;display:flex;gap:12px;color:#fff}
.contact__col{flex:1;font-size:5px;line-height:1.6}
.contact__col + .contact__col{border-left:1px solid rgba(255,255,255,.6);padding-left:10px}
.contact__title{font-weight:700;font-size:6px;line-height:1.3;margin-bottom:6px}
.contact__list{list-style:none}
.contact__list li{display:flex;align-items:center;gap:4px}
.contact__list li::before{content:"";width:4px;height:4px;border-radius:50%;background:#fff}

/* front cover */
.front .brand{left:56px;top:16px}
.front .brand__mark{width:28px;height:28px}
.front .brand__name{font-size:17px}
.front__photo{position:absolute;top:58px;left:0;right:0;height:166px;background:linear-gradient(135deg,#c9b39a,#8c8a86 45%,#5d6f7a)}
.front__ribbon{position:absolute;top:220px;left:22px;right:22px;background:var(--magenta);color:#fff;font-size:5.6px;font-weight:600;text-align:center;padding:3px 0}
.front__band{position:absolute;top:229px;left:0;right:0;height:82px;background:var(--teal)}
.front__headline{position:absolute;top:236px;left:8px;right:8px;text-align:center;color:#fff;font-weight:700;font-size:11px;line-height:1.15}
.front__formats{position:absolute;top:274px;left:20px;right:20px;background:var(--magenta);color:#fff;font-size:5.8px;font-weight:600;padding:5px 6px;line-height:1.4}
.front__funding{position:absolute;top:318px;left:18px;right:14px;display:flex;gap:8px;align-items:center;font-size:4.4px;line-height:1.4;color:var(--ink)}
.front__flag{width:26px;height:17px;background:#2b4a9e;flex:none}

/* inside */
.heading{position:absolute;color:var(--teal);font-weight:700;font-size:12px;letter-spacing:.3px}
.challenge__heading{left:12px;top:10px}
.challenge__body{position:absolute;left:12px;top:27px;width:136px;font-size:4.3px;line-height:1.45}
.accent{color:var(--magenta);font-weight:700}
.challenge__body ul{list-style:none;margin:2px 0 3px}
.challenge__body li::before{content:"• "}
.offer__band{position:absolute;top:126px;left:0;width:150px;height:56px;background:var(--teal);color:#fff;font-size:5.4px;font-weight:700;line-height:1.35;padding:8px 18px 0 12px}
.offers__heading{left:12px;top:190px}
.offers__list{position:absolute;top:208px;left:10px;width:128px;list-style:none;font-size:4.4px;line-height:1.4}
.offers__list li{display:flex;gap:4px;margin-bottom:6px}
.tick{flex:none;width:7px;height:7px}
.stats{position:absolute;top:228px;left:136px;width:110px;display:grid;grid-template-columns:1fr 1fr;gap:6px 4px}
.stat{display:flex;flex-direction:column;gap:1px}
.stat__row{display:flex;align-items:center;gap:3px}
.stat__icon{width:15px;height:15px;border:1.2px solid var(--magenta);border-radius:3px;background:#fff}
.stat__num{color:var(--teal-dark);font-weight:700;font-size:12px}
.stat__label{font-size:3.6px;font-weight:700;color:var(--ink);line-height:1.2}
.stripes{position:absolute;left:0;right:0;bottom:0;height:16px}

.involved__photo{position:absolute;top:0;left:0;right:0;height:112px;background:linear-gradient(90deg,#c8b7a6,#e3d8cc 45%,#ffffff 80%)}
.involved__heading{right:12px;top:26px}
.involved__list{position:absolute;top:44px;right:10px;width:140px;list-style:none;font-size:5px;line-height:1.35;text-align:right}
.involved__list li{display:flex;justify-content:flex-end;gap:4px;margin-bottom:5px}
.visit{position:absolute;top:126px;left:106px;right:0;height:56px;background:var(--teal);color:#fff;padding:9px 8px 0 10px}
.visit__lead{font-size:6.3px;font-weight:600}
.visit__big{font-size:10px;font-weight:700}
.visit__url{font-size:6.5px;font-weight:500}
.who__heading{right:12px;top:196px}
.who__lead{position:absolute;top:214px;right:12px;width:150px;text-align:right;font-size:5.6px;font-weight:700;line-height:1.35}
.who__grid{position:absolute;top:244px;left:8px;right:8px;display:grid;grid-template-columns:1fr 1fr;gap:6px 10px}
.who__title{font-size:4.6px;font-weight:700;color:var(--magenta);padding-bottom:2px;border-bottom:1px solid var(--teal);margin-bottom:3px}
.who__text{display:flex;gap:3px;font-size:4.2px;line-height:1.4}
.hexes{position:absolute;top:0;left:0;width:500px;height:354px;pointer-events:none}
</style>
</head>
<body>

<!-- OUTSIDE: back + front cover -->
<section class="spread spread--outside">
  <article class="page back">
    <div class="brand"><span class="brand__mark"></span><span class="brand__name">PS Forum</span></div>
    <h2 class="partners__title">PARTNERS</h2>
    <div class="partners__grid">
      <span class="partners__badge"></span><span class="partners__badge"></span><span class="partners__badge"></span><span class="partners__badge"></span>
      <span class="partners__badge"></span><span class="partners__badge"></span><span class="partners__badge"></span><span class="partners__badge"></span>
      <span class="partners__badge"></span><span class="partners__badge"></span><span class="partners__badge"></span><span class="partners__badge"></span>
    </div>
    <div class="back__rule"></div>
    <div class="back__contact">
      <div class="contact__col">
        <p class="contact__title">GOT YOUR ATTENTION?<br>STAY IN TOUCH!</p>
        <ul class="contact__list">
          <li>@PSForum_eu</li>
          <li>@PSForum.eu</li>
          <li>PS Forum</li>
          <li>https://psforum.example/</li>
          <li>info@psforum.example</li>
        </ul>
      </div>
      <div class="contact__col">
        <p class="contact__title">DO YOU STILL<br>HAVE QUESTIONS?</p>
        <p>Feel free to contact us at<br>info@psforum.example</p>
        <p style="margin-top:6px">A member of the team will<br>make her/his best to reply<br>as soon as possible.</p>
      </div>
    </div>
  </article>

  <article class="page front">
    <div class="brand"><span class="brand__mark"></span><span class="brand__name">PS Forum</span></div>
    <div class="front__photo" role="img" aria-label="Photo of students and a teacher working together around a table"></div>
    <div class="front__band"></div>
    <p class="front__ribbon">A HIGH-QUALITY CAPACITY-BUILDING PROGRAMME ON</p>
    <h1 class="front__headline">GENDER EQUALITY IN RESEARCH,<br>INNOVATION AND HIGHER EDUCATION</h1>
    <p class="front__formats">IN PERSON-TRAININGS | WORKSHOPS | SUMMER SCHOOLS |<br>DOCCS | WEBINARS | TRAIN-THE-TRAINERS SESSIONS</p>
    <div class="front__funding">
      <span class="front__flag"></span>
      <p>"THIS PROJECT HAS RECEIVED FUNDING FROM THE UNION FRONTIER 2020 RESEARCH AND INNOVATION PROGRAMME UNDER GRANT AGREEMENT NO 000000"</p>
    </div>
  </article>
</section>

<!-- INSIDE: challenge/offers + involvement -->
<section class="spread spread--inside">
  <article class="page inside-left">
    <h2 class="heading challenge__heading">THE CHALLENGE</h2>
    <div class="challenge__body">
      <p class="accent">CURRENTLY, THERE ARE MANY PROGRAMMES, PROJECTS AND A GREAT GAINED KNOWLEDGE AND EXPERIENCE, BUT:</p>
      <ul>
        <li>Gender analysis remains rarely appropriated within research projects</li>
        <li>Large differences among research performing organisations in various countries</li>
        <li>Small proportion of researchers and practitioners are familiar with theoretical and methodological concepts of gender and feminist scholarship</li>
      </ul>
      <p class="accent">NEED: A HOLISTIC APPROACH TO STRUCTURAL CHANGE FOR GENDER EQUALITY IN R&amp;I</p>
    </div>
    <p class="offer__band">THE PARITY SKILLS FORUM PROJECT OFFERS HIGH QUALITY CAPACITY-BUILDING PROGRAMME ON GENDER EQUALITY IN RESEARCH, INNOVATION AND HIGHER EDUCATION</p>
    <h2 class="heading offers__heading">TRAINING OFFERS</h2>
    <ul class="offers__list">
      <li><svg class="tick" viewBox="0 0 10 10"><circle cx="5" cy="5" r="4.3" fill="none" stroke="#c4286b"/><path d="M3 5.2l1.5 1.5L7.2 3.6" fill="none" stroke="#c4286b" stroke-width="1.2"/></svg><span>TRAININGS ARE OFFERED FOR FREE TO THOSE INTERESTED TO UNDERSTAND AND CONSIDER GENDER EQUALITY AND DIMENSION AS AN INTEGRAL PART OF RESEARCH AND INNOVATION.</span></li>
      <li><svg class="tick" viewBox="0 0 10 10"><circle cx="5" cy="5" r="4.3" fill="none" stroke="#c4286b"/><path d="M3 5.2l1.5 1.5L7.2 3.6" fill="none" stroke="#c4286b" stroke-width="1.2"/></svg><span>FIND THE OFFER WHICH SUITS YOU BEST AND REGISTER ON https://psforum.example/</span></li>
      <li><svg class="tick" viewBox="0 0 10 10"><circle cx="5" cy="5" r="4.3" fill="none" stroke="#c4286b"/><path d="M3 5.2l1.5 1.5L7.2 3.6" fill="none" stroke="#c4286b" stroke-width="1.2"/></svg><span>THERE ARE DIFFERENT DATES AND LOCATIONS</span></li>
      <li><svg class="tick" viewBox="0 0 10 10"><circle cx="5" cy="5" r="4.3" fill="none" stroke="#c4286b"/><path d="M3 5.2l1.5 1.5L7.2 3.6" fill="none" stroke="#c4286b" stroke-width="1.2"/></svg><span>COURSE LANGUAGE: ENGLISH</span></li>
      <li><svg class="tick" viewBox="0 0 10 10"><circle cx="5" cy="5" r="4.3" fill="none" stroke="#c4286b"/><path d="M3 5.2l1.5 1.5L7.2 3.6" fill="none" stroke="#c4286b" stroke-width="1.2"/></svg><span>PARTICIPATION IS FREE THANKS TO THE FUND.</span></li>
    </ul>
    <div class="stats">
      <div class="stat"><div class="stat__row"><span class="stat__icon"></span><span class="stat__num">28</span></div><span class="stat__label">TRAINING OFFERS</span></div>
      <div class="stat"><div class="stat__row"><span class="stat__icon"></span><span class="stat__num">12</span></div><span class="stat__label">WORKSHOPS</span></div>
      <div class="stat"><div class="stat__row"><span class="stat__icon"></span><span class="stat__num">3</span></div><span class="stat__label">SUMMER SCHOOLS</span></div>
      <div class="stat"><div class="stat__row"><span class="stat__icon"></span><span class="stat__num">2</span></div><span class="stat__label">DISTRIBUTED OPEN COLLABORATIVE COURSES</span></div>
      <div class="stat"><div class="stat__row"><span class="stat__icon"></span><span class="stat__num">2</span></div><span class="stat__label">TRAIN-THE-TRAINERS' SESSIONS</span></div>
      <div class="stat"><div class="stat__row"><span class="stat__icon"></span><span class="stat__num">12</span></div><span class="stat__label">WEBINARS</span></div>
    </div>
    <svg class="stripes" viewBox="0 0 250 16" preserveAspectRatio="none"><polygon points="0,6 250,12 250,16 0,16" fill="#22b2c3"/><polygon points="0,10 250,4 250,16 0,16" fill="#c4286b"/></svg>
  </article>

  <article class="page inside-right">
    <div class="involved__photo" role="img" aria-label="Photo of a teacher talking with pupils"></div>
    <h2 class="heading involved__heading">GET INVOLVED</h2>
    <ul class="involved__list">
      <li><span>Take part in one or more offered<br>trainings</span><svg class="tick" viewBox="0 0 10 10"><rect x=".6" y=".6" width="8.8" height="8.8" rx="2" fill="none" stroke="#c4286b"/><path d="M3 5.2l1.5 1.5L7.2 3.6" fill="none" stroke="#c4286b" stroke-width="1.2"/></svg></li>
      <li><span>Become a gender trainer</span><svg class="tick" viewBox="0 0 10 10"><rect x=".6" y=".6" width="8.8" height="8.8" rx="2" fill="none" stroke="#c4286b"/><path d="M3 5.2l1.5 1.5L7.2 3.6" fill="none" stroke="#c4286b" stroke-width="1.2"/></svg></li>
      <li><span>Become a host institution to the topic<br>of your preference</span><svg class="tick" viewBox="0 0 10 10"><rect x=".6" y=".6" width="8.8" height="8.8" rx="2" fill="none" stroke="#c4286b"/><path d="M3 5.2l1.5 1.5L7.2 3.6" fill="none" stroke="#c4286b" stroke-width="1.2"/></svg></li>
      <li><span>Be part of the pan European gender<br>trainers' network</span><svg class="tick" viewBox="0 0 10 10"><rect x=".6" y=".6" width="8.8" height="8.8" rx="2" fill="none" stroke="#c4286b"/><path d="M3 5.2l1.5 1.5L7.2 3.6" fill="none" stroke="#c4286b" stroke-width="1.2"/></svg></li>
    </ul>
    <div class="visit">
      <p class="visit__lead">VISIT THE WEBSITE AND</p>
      <p class="visit__big">FIND OUT MORE</p>
      <p class="visit__url">https://psforum.example/</p>
    </div>
    <h2 class="heading who__heading">WHO IS IT FOR?</h2>
    <p class="who__lead">ANYONE INTERESTED TO GENDER EQUALITY, BUT ALSO:</p>
    <div class="who__grid">
      <div><p class="who__title">HR PROFESSIONALS</p><p class="who__text"><svg class="tick" viewBox="0 0 10 10"><rect x=".6" y=".6" width="8.8" height="8.8" rx="2" fill="none" stroke="#c4286b"/><path d="M3 5.2l1.5 1.5L7.2 3.6" fill="none" stroke="#c4286b" stroke-width="1.2"/></svg><span>Integration and establishment of gender-sensitive and fair recruitment and career management processes in organisations</span></p></div>
      <div><p class="who__title">GENDER TRAINERS &amp; EXPERTS</p><p class="who__text"><svg class="tick" viewBox="0 0 10 10"><rect x=".6" y=".6" width="8.8" height="8.8" rx="2" fill="none" stroke="#c4286b"/><path d="M3 5.2l1.5 1.5L7.2 3.6" fill="none" stroke="#c4286b" stroke-width="1.2"/></svg><span>Train-the-trainers sessions for the development of new skills</span></p></div>
      <div><p class="who__title">RESEARCHERS</p><p class="who__text"><svg class="tick" viewBox="0 0 10 10"><rect x=".6" y=".6" width="8.8" height="8.8" rx="2" fill="none" stroke="#c4286b"/><path d="M3 5.2l1.5 1.5L7.2 3.6" fill="none" stroke="#c4286b" stroke-width="1.2"/></svg><span>Training to integrate the gender dimension in their research and deepening their understanding of gender issues in R&amp;I</span></p></div>
      <div><p class="who__title">RESEARCH PERFORMING ORGANISATIONS</p><p class="who__text"><svg class="tick" viewBox="0 0 10 10"><rect x=".6" y=".6" width="8.8" height="8.8" rx="2" fill="none" stroke="#c4286b"/><path d="M3 5.2l1.5 1.5L7.2 3.6" fill="none" stroke="#c4286b" stroke-width="1.2"/></svg><span>Recommendations for influencing the internal policies and practices of the organisations towards gender equality</span></p></div>
    </div>
    <svg class="stripes" viewBox="0 0 250 16" preserveAspectRatio="none"><polygon points="0,12 250,6 250,16 0,16" fill="#22b2c3"/><polygon points="0,4 250,10 250,16 0,16" fill="#c4286b"/></svg>
  </article>

  <svg class="hexes" viewBox="0 0 500 354">
    <g role="img" aria-label="Photo of two children smiling at a desk">
      <polygon points="212,-24 262,4 262,82 212,110 162,82 162,4" fill="#d9c3a8" stroke="#c4286b" stroke-width="3"/>
    </g>
    <g role="img" aria-label="Photo of open books and notes on a table">
      <polygon points="186,120 236,148 236,204 186,232 136,204 136,148" fill="#8d8a84" stroke="#c4286b" stroke-width="3"/>
    </g>
    <g role="img" aria-label="Black and white photo of people in a workshop">
      <polygon points="314,112 360,138 360,182 314,208 268,182 268,138" fill="#b8bcbf" stroke="#c4286b" stroke-width="3"/>
    </g>
  </svg>
</section>

</body>
</html>
```